Business Card Design to Compliment attached Letterhead

I am looking for a really nice business card for my new business launch. I develop Excel based applications to support administrative and operational processes. I have attached my letterhead so you have an idea what the components should look like. I tried uploading the various components into the "Design your own" section, but they looked really rough, so I am looking for someone to be able to come up with a nice crisp version of the tetras square and the Company Name styling that will compliment my letterhead; and then put all of this into a business card design that is crisp, clean and professional looking. I am considering using spot gloss, because I think it will add an extra touch of class.

Industry/Entity Type

Business

Contact Information for Business Card

Kembrin Consulting, Grid Remedies for Routine Snags, Marta Hollowby, Business Systems Analyst, Spreadsheet Specialist, 0493 058 274, marta@kembrinconsulting.com.au www.kembrinconsulting.com.au

Requirements
Must have
• I want to use the same colors as the attached file and keep the fonts used for "Kembrin" and "Consulting"
• I need the Tetras square to be re-created. I did it myself using photoshop and it is pretty rough. I need it to be crisp and clean and professional looking.
• Please include my name, title, phone, email, web address and "Grid Remedies to Routine Snags"
Nice to have
• So far I have liked the designs that are a little bit different. I want people to look at my card and say "Nice Card"
Should not have
• I don't like the see-through format.
• Do not include any information about Arvel Designs or the address
• Please dont use my version of the tetras square, it is fuzzy and poorly drawn (I did it myself), I need it to be crisp, and clean otherwise it will spoil the effect of my nice new cards.

```html
<!DOCTYPE html>
<html lang="en">
<head>
<meta charset="utf-8">
<title>Kembrin Consulting – Business Card</title>
<link rel="stylesheet" href="https://fonts.googleapis.com/css2?family=Source+Sans+3:wght@400;600;700&display=swap">
<style>
  :root {
    --purple: #6c3795;
    --blue: #1a7cc1;
    --ink: #5d5d5d;
    --card: #ffffff;
    --backdrop: #e7e4df;
  }
  * { margin: 0; padding: 0; box-sizing: border-box; }
  html, body {
    width: 1200px; height: 1000px; overflow: hidden;
    background: var(--backdrop);
    font-family: "Source Sans 3", "Myriad Pro", sans-serif;
  }
  .business-card {
    position: absolute; left: 265px;
    width: 665px; height: 397px;
    background: var(--card);
    box-shadow: 0 2px 6px rgba(0,0,0,0.18);
    overflow: hidden;
  }
  .business-card--upper { top: 73px; }
  .business-card--lower { top: 532px; }

  .brand-square {
    position: absolute; left: 50px; top: 58px;
    width: 110px; height: 110px;
    background: var(--blue);
  }
  .brand-name {
    position: absolute; left: 190px; top: 84px;
    font-size: 40px; font-weight: 700; line-height: 1;
    color: var(--purple);
    white-space: nowrap;
  }

  .contact-list {
    position: absolute; left: 27px; top: 235px;
    list-style: none;
    font-size: 16.5px; color: var(--ink);
  }
  .contact-list li {
    display: flex; align-items: center;
    height: 23.5px;
  }
  .contact-list svg { width: 14px; height: 14px; margin-right: 8px; flex: none; }

  .tagline {
    position: absolute; left: 27px; top: 326px;
    font-size: 16.5px; font-weight: 700; color: var(--ink);
  }

  .holder {
    position: absolute; right: 28px; top: 236px;
    text-align: right; color: var(--ink);
  }
  .holder-name {
    font-size: 22px; font-weight: 700; color: var(--blue);
    line-height: 26px; margin-bottom: 3px;
  }
  .holder-role { font-size: 17.5px; line-height: 21px; }
  .accent-bar {
    position: absolute; right: 0; top: 239px;
    width: 18px; height: 64px; background: var(--blue);
  }

  .footer-band {
    position: absolute; left: 0; bottom: 0;
    width: 665px; height: 29px; display: block;
  }
</style>
</head>
<body>

<section class="business-card business-card--upper">
  <div class="brand-square"></div>
  <div class="brand-name">Kembrin Consulting</div>
  <ul class="contact-list">
    <li><svg viewBox="0 0 16 16"><path d="M4 1.5l2.5 3-1.6 1.6c.8 1.9 2.2 3.3 4.1 4.1l1.6-1.6 3 2.5-1.6 2.4C7 13 3 9 1.5 3.1z" fill="var(--purple)"/></svg>0493 058 274</li>
    <li><svg viewBox="0 0 16 16"><rect x="1" y="3" width="14" height="10" fill="var(--purple)"/><path d="M1.5 3.5L8 9l6.5-5.5" fill="none" stroke="#fff" stroke-width="1.2"/></svg>marta@kembrinconsulting.com.au</li>
    <li><svg viewBox="0 0 16 16"><g fill="none" stroke="var(--purple)" stroke-width="1.3"><circle cx="8" cy="8" r="6.3"/><ellipse cx="8" cy="8" rx="2.8" ry="6.3"/><path d="M1.7 8h12.6M2.8 4.8h10.4M2.8 11.2h10.4"/></g></svg>www.kembrinconsulting.com.au</li>
  </ul>
  <p class="tagline">Grid Remedies for Routine Snags</p>
  <div class="holder">
    <p class="holder-name">Marta Hollowby</p>
    <p class="holder-role">Business Systems Analyst</p>
    <p class="holder-role">Spreadsheet Specialist</p>
  </div>
  <div class="accent-bar"></div>
  <svg class="footer-band" viewBox="0 0 665 29" preserveAspectRatio="none">
    <polygon points="0,0 372,0 345,29 0,29" fill="var(--purple)"/>
    <polygon points="379,0 665,0 665,29 352,29" fill="var(--blue)"/>
  </svg>
</section>

<section class="business-card business-card--lower">
  <div class="brand-square"></div>
  <div class="brand-name">Kembrin Consulting</div>
  <ul class="contact-list">
    <li><svg viewBox="0 0 16 16"><path d="M4 1.5l2.5 3-1.6 1.6c.8 1.9 2.2 3.3 4.1 4.1l1.6-1.6 3 2.5-1.6 2.4C7 13 3 9 1.5 3.1z" fill="var(--purple)"/></svg>0493 058 274</li>
    <li><svg viewBox="0 0 16 16"><rect x="1" y="3" width="14" height="10" fill="var(--purple)"/><path d="M1.5 3.5L8 9l6.5-5.5" fill="none" stroke="#fff" stroke-width="1.2"/></svg>marta@kembrinconsulting.com.au</li>
    <li><svg viewBox="0 0 16 16"><g fill="none" stroke="var(--purple)" stroke-width="1.3"><circle cx="8" cy="8" r="6.3"/><ellipse cx="8" cy="8" rx="2.8" ry="6.3"/><path d="M1.7 8h12.6M2.8 4.8h10.4M2.8 11.2h10.4"/></g></svg>www.kembrinconsulting.com.au</li>
  </ul>
  <p class="tagline">Grid Remedies for Routine Snags</p>
  <div class="holder">
    <p class="holder-name">Marta Hollowby</p>
    <p class="holder-role">Business Systems Analyst</p>
    <p class="holder-role">Spreadsheet Specialist</p>
  </div>
  <div class="accent-bar"></div>
  <svg class="footer-band" viewBox="0 0 665 29" preserveAspectRatio="none">
    <polygon points="0,0 372,0 345,29 0,29" fill="var(--purple)"/>
    <polygon points="379,0 665,0 665,29 352,29" fill="var(--blue)"/>
  </svg>
</section>

</body>
</html>
```